Dashboard Elements

Hello – looking for someone to create dashboard elements.
I’ve already basically designed all these elements – but I need someone to take what I’ve designed and make it look like an actual dashboard UI, like an app - assuming using some kind of dashboard UI kit (but however you would like to get it done is fine). It can look just like mine or try something different, as long as it matches the color scheme webpage that I’m going to out it on – see the page here. I’m ok with making it dark, maybe that would look better – again as long as it matches the webpage (https://www.plankora.com/file/7QxVbN2kLmRtWp4Ya8Hc3J/Webpage-with-placeholders?node-id=0%3A1). Please note, you do not need to put anything on the webpage or do anything with this Plankora file, this is just a reference so you can color/stylize it accordingly.

The attached Powerpoint file has everything you need - make sure to zoom all the way out to see everything on the slides.

Here are the Dashboard elements needed (this will all make sense when you look at the PPT):
Dashboard 1
Dashboard 1 – expanded view A
Dashboard 1 – expanded view B
View Source button by itself
Source Document Viewer 1 and 2 (these are exactly the same just with a different image inside)*
Dashboard 2 (only slightly different than Dashboard 1, just extended with extra headings
Table of Contents
Searchbar and Source Doc by itself
*the documents in the source document viewers should still look like documents - they don’t need to look like part of the UI, because this is a document viewer – you can restyle/recolor if necessary or just leave these as is.
- Colors must match color scheme of webpage, attached and on Plankora link (images there currently are only placeholders) – ok to go dark as long as it matches
- Must look sleek, clean, realistic
- Don’t add any pictures of people or change the text.
- In case it’s not clear, this is what I mean by the concept of Dashboard UI - https://www.quillbary.com/shard/s2/sh/9a4c1e27-b835-4f02-a7d6-5c0e81b3f947/e72b6a09c4d1f5830b9e6a2d7c4f1e58
- Must be sent in an editable file, I may need to be edit text and other elements
- If you are going to send a sample, please make sure it’s part of the dashboard itself, not just the table of contents etc

Ideally hoping to find someone I can continue working with as I'll have a lot more graphic design work needed coming up.

Thank you!

```html
<!DOCTYPE html>
<html lang="en">
<head>
<meta charset="utf-8">
<title>CareLedger – C-CDA Compendium Dashboard Board</title>
<link href="https://fonts.googleapis.com/css2?family=Poppins:wght@300;400;500;600;700&display=swap" rel="stylesheet">
<style>
:root{
  --page:#1c1a3e;
  --heading:#8c7fe6;
  --heading-accent:#a9b4ff;
  --shell:#191640;
  --main:#241f52;
  --row-a:#35306b;
  --row-b:#29255c;
  --row-head:#15123a;
  --expand:#221d4e;
  --card:#16133a;
  --teal:#2bc7b4;
  --cyan:#2ab8cc;
  --blue:#1c8fd8;
  --purple:#7b6be0;
  --text:#ffffff;
  --muted:#c9c6ea;
}
*{box-sizing:border-box;margin:0;padding:0}
html,body{width:1200px;height:4159px;overflow:hidden}
body{
  position:relative;
  background:radial-gradient(circle at 100% 60%,rgba(120,80,200,.25),transparent 40%),
             radial-gradient(circle at 0% 30%,rgba(70,60,170,.25),transparent 40%),var(--page);
  font-family:'Poppins',sans-serif;color:var(--text);
}
.abs{position:absolute}
.board-title{position:absolute;left:0;width:1200px;text-align:center;font-size:34px;font-weight:600;color:var(--heading);line-height:44px}
.board-title span{color:var(--heading-accent)}
.frame{position:absolute;left:31px;width:1138px;overflow:hidden;background:var(--main)}
.frame.bordered{border:1px solid #4a448a}

/* shell */
.topbar{position:absolute;left:0;top:0;width:100%;height:90px;background:var(--shell)}
.brand-mark{position:absolute;left:47px;top:29px;width:34px;height:34px;border-radius:6px;background:var(--teal)}
.brand-name{position:absolute;left:123px;top:24px;font-size:24px;font-weight:500;color:var(--teal);line-height:30px}
.tagline{position:absolute;left:123px;top:60px;font-size:10px;font-weight:500;letter-spacing:.2px;text-transform:uppercase}
.apps{position:absolute;left:882px;top:40px}
.badge{position:absolute;left:934px;top:38px;width:37px;height:20px;border-radius:10px;background:var(--blue);font-size:9px;line-height:20px;text-align:center;font-weight:600}
.avatar{position:absolute;left:990px;top:38px;width:20px;height:20px;border-radius:4px;background:#c9b8a8}
.user{position:absolute;left:1022px;top:38px;font-size:11px;line-height:20px}
.sidebar{position:absolute;left:0;top:90px;width:220px;bottom:0;background:var(--shell)}
.side-label{position:absolute;left:34px;font-size:14px;font-weight:500}
.nav-item{position:absolute;left:40px;display:flex;align-items:center;gap:12px;font-size:14px}
.nav-item i{width:26px;height:26px;border-radius:6px;background:#2c2860;display:flex;align-items:center;justify-content:center}
.nav-item i b{width:12px;height:12px;background:#fff;border-radius:2px;display:block}
.nav-item.active{color:var(--teal)}
.nav-item.active i b{background:var(--teal)}
.footer{position:absolute;left:220px;right:0;height:64px;background:var(--shell)}
.footer .copy{position:absolute;left:27px;top:22px;font-size:13px;font-weight:500}
.footer .fbrand{position:absolute;right:35px;top:22px;font-size:13px;color:var(--teal);font-weight:500}

.crumb-icon{position:absolute;left:247px;top:111px;width:32px;height:32px;border-radius:7px;background:#34306a;display:flex;align-items:center;justify-content:center}
.crumb{position:absolute;left:291px;top:114px;font-size:19px;font-weight:600;line-height:26px}
.crumb .lnk{color:var(--teal);font-weight:500}
.print{position:absolute;left:780px;top:111px;width:34px;height:34px;border-radius:7px;background:#34306a;display:flex;align-items:center;justify-content:center}
.idsearch{position:absolute;left:830px;top:111px;width:273px;height:36px;border-radius:5px;background:#34306a;font-size:11px;color:var(--muted);line-height:36px;padding-left:12px}
.idsearch .sel{position:absolute;left:150px;color:var(--cyan);font-size:9px;border-left:1px solid var(--cyan);padding-left:6px;line-height:12px;top:12px}
.sbtn{position:absolute;right:6px;top:7px;width:22px;height:22px;border-radius:4px;background:var(--cyan);display:flex;align-items:center;justify-content:center}
.profile{position:absolute;left:247px;top:171px;font-size:17px;line-height:24px}
.profile .k,.updated .k{color:var(--teal)}
.updated{position:absolute;right:35px;top:171px;font-size:17px;line-height:24px}
.stat{position:absolute;top:205px;width:142px;height:57px;border-radius:6px;padding:11px 0 0 16px}
.stat .lbl{font-size:9px;letter-spacing:1px;line-height:12px}
.stat .val{font-size:13px;font-weight:600;letter-spacing:3px;line-height:18px;margin-top:4px}
.stat .ic{position:absolute;right:14px;top:13px;width:30px;height:30px;border-radius:50%;background:rgba(20,18,60,.75)}
.stat.raf{left:247px;background:var(--blue)}
.stat.cond{left:415px;background:var(--teal)}
.stat.idn{left:583px;background:var(--purple)}
.hcc{position:absolute;left:247px;top:289px;font-size:19px;color:var(--teal);font-weight:600;line-height:24px}
.section{position:absolute;left:247px;font-size:14px;font-weight:600;line-height:20px}
.mini-search{position:absolute;left:937px;width:166px;height:29px;border-radius:5px;background:#34306a;font-size:10px;color:var(--muted);line-height:29px;padding-left:16px}
.mini-search .sbtn{top:4px;right:4px;width:21px;height:21px}

/* tables */
.tbl{position:absolute}
.tbl .hd,.tbl .rw{display:grid;grid-template-columns:var(--cols);align-items:center;padding-left:var(--pl)}
.tbl .hd{background:var(--row-head);font-weight:500}
.tbl .rw:nth-child(even){background:var(--row-a)}
.tbl .rw:nth-child(odd){background:var(--row-b)}
.tbl .rw.open{background:var(--expand)}
.tbl .code{color:var(--cyan)}
.tbl .raf{color:var(--teal)}
.tbl .rw.open .cond{font-weight:600}
.tbl .rw.open .raf{font-weight:600}
.tbl.small{font-size:10.5px;--cols:113px 437px 110px 86px 1fr;--pl:18px;left:247px;width:856px}
.tbl.small .hd{height:42px}
.tbl.small .rw{height:44px}
.btn{display:flex;align-items:center;justify-content:space-between;border-radius:3px;background:linear-gradient(90deg,var(--blue),var(--teal));color:#fff;font-weight:500}
.btn.close{background:var(--purple)}
.tbl.small .btn{width:79px;height:24px;padding:0 10px 0 14px;font-size:10px}
.tbl.large{font-size:14px;left:0;width:1138px}
.tbl.large .hd{height:62px}
.tbl.large .rw{height:58px}
.tbl.large .btn{width:105px;height:34px;padding:0 14px 0 20px;font-size:15px}
.caret{width:0;height:0;border-left:4px solid transparent;border-right:4px solid transparent;border-top:5px solid currentColor;display:inline-block;margin-left:6px;vertical-align:middle}
.tri-r{width:0;height:0;border-top:4px solid transparent;border-bottom:4px solid transparent;border-left:5px solid #fff;display:inline-block}
.tri-l{width:0;height:0;border-top:4px solid transparent;border-bottom:4px solid transparent;border-right:5px solid #fff;display:inline-block}

.note{position:absolute;line-height:20px}
.note b{color:var(--teal);font-weight:600}
.src{position:absolute;background:var(--card);border-radius:8px}
.src.glow{border:1.5px solid var(--teal);box-shadow:0 0 22px rgba(43,199,180,.45)}
.src .t{position:absolute;line-height:20px}
.src .s{position:absolute;color:var(--teal);line-height:20px}
.src .view{position:absolute;color:var(--teal);line-height:20px}
.src .doc{position:absolute;border-radius:8px;background:#221e52;display:flex;align-items:center;justify-content:center}
.src .kv{position:absolute;line-height:20px}
.src .kv span{color:var(--teal)}

.pager{position:absolute;display:flex;align-items:center;font-size:10px}
.pager .sel{margin-left:10px;width:26px;height:24px;border-radius:3px;background:#34306a;display:flex;align-items:center;justify-content:center;font-size:9px}
.pager .pg{width:26px;height:26px;border-radius:3px;display:flex;align-items:center;justify-content:center;margin-left:13px;background:#34306a}
.pager .pg.next{background:var(--cyan)}
</style>
</head>
<body>

<svg width="0" height="0" style="position:absolute">
  <defs>
    <symbol id="doc" viewBox="0 0 12 16"><path d="M0 1.5A1.5 1.5 0 0 1 1.5 0H8l4 4v10.5A1.5 1.5 0 0 1 10.5 16h-9A1.5 1.5 0 0 1 0 14.5z" fill="#2bc7b4"/><path d="M8 0v4h4" fill="#1d7f76"/></symbol>
    <symbol id="mag" viewBox="0 0 12 12"><circle cx="5" cy="5" r="3.6" fill="none" stroke="#15123a" stroke-width="1.6"/><path d="M7.7 7.7 11 11" stroke="#15123a" stroke-width="1.6"/></symbol>
    <symbol id="grid" viewBox="0 0 16 16" fill="#2ab8cc"><circle cx="2" cy="2" r="1.5"/><circle cx="8" cy="2" r="1.5"/><circle cx="14" cy="2" r="1.5"/><circle cx="2" cy="8" r="1.5"/><circle cx="8" cy="8" r="1.5"/><circle cx="14" cy="8" r="1.5"/><circle cx="2" cy="14" r="1.5"/><circle cx="8" cy="14" r="1.5"/><circle cx="14" cy="14" r="1.5"/></symbol>
    <symbol id="tiles" viewBox="0 0 12 12" fill="#2bc7b4"><rect width="5" height="5" rx="1"/><rect x="7" width="5" height="5" rx="1"/><rect y="7" width="5" height="5" rx="1"/><rect x="7" y="7" width="5" height="5" rx="1"/></symbol>
    <symbol id="printer" viewBox="0 0 14 14" fill="#2bc7b4"><rect x="3" y="1" width="8" height="4" rx="1"/><rect x="1" y="5" width="12" height="6" rx="1.5"/><rect x="4" y="9" width="6" height="4" fill="#fff"/></symbol>
  </defs>
</svg>

<!-- ============ Board 1 ============ -->
<h2 class="board-title" style="top:46px">Dashboard 1, Created with <span>Plankora</span></h2>

<section class="frame" style="top:103px;height:776px">
  <div class="topbar">
    <div class="brand-mark"></div>
    <div class="brand-name">CareLedger</div>
    <div class="tagline">Each patients' full medical history, summary and analysis in one comprehensive health record</div>
    <svg class="apps" width="16" height="16"><use href="#grid"/></svg>
    <div class="badge">27</div>
    <div class="avatar"></div>
    <div class="user">Lina Admin <span class="caret"></span></div>
  </div>
  <nav class="sidebar">
    <div class="side-label" style="top:33px">Main</div>
    <div class="nav-item" style="top:56px"><i><b></b></i>Dashboard</div>
    <div class="nav-item" style="top:99px"><i><b></b></i>Employee</div>
    <div class="nav-item" style="top:143px"><i><b></b></i>Document</div>
    <div class="nav-item" style="top:187px"><i><b></b></i>Appointment</div>
    <div class="nav-item" style="top:230px"><i><b></b></i>Surveillance</div>
    <div class="nav-item active" style="top:274px"><i><b></b></i>Reports</div>
    <div class="side-label" style="top:333px">Support</div>
    <div class="nav-item" style="top:367px"><i><b></b></i>Settings</div>
    <div class="nav-item" style="top:411px"><i><b></b></i>Tutorial</div>
  </nav>

  <div class="crumb-icon"><svg width="14" height="14"><use href="#tiles"/></svg></div>
  <div class="crumb"><span class="lnk">Reports</span> <span style="font-size:13px">▶</span> C-CDA Compendium</div>
  <div class="print"><svg width="16" height="16"><use href="#printer"/></svg></div>
  <div class="idsearch">Type ID Number here <span class="sel">ID Number <span class="caret"></span></span><span class="sbtn"><svg width="11" height="11"><use href="#mag"/></svg></span></div>

  <div class="profile"><span class="k">Patient Profile</span>&nbsp;&nbsp; Nora Vale | Female | 70 Years Old | 01-11-1951</div>
  <div class="updated"><span class="k">Last Updated:</span> May 24, 2021</div>

  <div class="stat raf"><div class="lbl">R A F</div><div class="val">2.362</div><div class="ic"></div></div>
  <div class="stat cond"><div class="lbl">Condition</div><div class="val">8</div><div class="ic"></div></div>
  <div class="stat idn"><div class="lbl">ID Number</div><div class="val" style="letter-spacing:1px">7326472</div><div class="ic"></div></div>

  <div class="hcc">▾ HCC Summary</div>
  <div class="section" style="top:329px">Previously Known ICD-10 Code</div>
  <div class="mini-search" style="top:320px">Search<span class="sbtn"><svg width="10" height="10"><use href="#mag"/></svg></span></div>

  <div class="tbl small" style="top:365px">
    <div class="hd"><span>ICD-10 CODE <span class="caret"></span></span><span>CONDITION <span class="caret"></span></span><span>CATEGORY <span class="caret"></span></span><span>RAF <span class="caret"></span></span><span>ACTION</span></div>
    <div class="rw"><span class="code">J44.9</span><span>Chronic Obstructive Pulmonary Disease</span><span>111</span><span class="raf">0.335</span><span class="btn">Detail <span class="caret"></span></span></div>
    <div class="rw"><span class="code">F33.1</span><span>Chronic Kidney Disease, Moderate (Stage 3)</span><span>138</span><span class="raf">0.069</span><span class="btn">Detail <span class="caret"></span></span></div>
    <div class="rw"><span class="code">F33.0</span><span>Major Deppresive Disorder, Recurrent, Mild</span><span>59</span><span class="raf">0.309</span><span class="btn">Detail <span class="caret"></span></span></div>
    <div class="rw"><span class="code">I42.9</span><span>Cardiomyopathy</span><span>85</span><span class="raf">0.447</span><span class="btn">Detail <span class="caret"></span></span></div>
    <div class="rw"><span class="code">E11.36</span><span>Type 2 Diabetes Mellitus with Diabetic Cataract</span><span>18</span><span class="raf">0.302</span><span class="btn">Detail <span class="caret"></span></span></div>
  </div>

  <div class="pager" style="left:898px;top:650px">Show Row <span class="sel">6 <span class="caret" style="margin-left:3px"></span></span><span class="pg"><span class="tri-l"></span></span><span class="pg next"><span class="tri-r"></span></span></div>

  <footer class="footer" style="top:712px"><span class="copy">© 2021 - All Rights Licensed</span><span class="fbrand">CareLedger</span></footer>
</section>

<!-- ============ Expanded View A ============ -->
<h2 class="board-title" style="top:915px">Dashboard 1 - Expanded View A</h2>

<section class="frame bordered" style="top:993px;height:578px;background:var(--expand)">
  <div class="tbl large" style="top:3px;--cols:150px 580px 147px 114px 1fr;--pl:26px">
    <div class="hd"><span>ICD-10 CODE <span class="caret"></span></span><span>CONDITION <span class="caret"></span></span><span>CATEGORY <span class="caret"></span></span><span>RAF <span class="caret"></span></span><span>ACTION</span></div>
    <div class="rw"><span class="code">170.0</span><span>Aortic Atherosclerosis</span><span>108</span><span class="raf">0.298</span><span class="btn">Detail <span class="caret"></span></span></div>
    <div class="rw"><span class="code">F33.1</span><span>Major Deppresive Disorder, Recurrent, Moderate</span><span>58</span><span class="raf">0.309</span><span class="btn">Detail <span class="caret"></span></span></div>
    <div class="rw"><span class="code">148.2</span><span>Chronic Atrial Fibrillation</span><span>96</span><span class="raf">0.268</span><span class="btn">Detail <span class="caret"></span></span></div>
    <div class="rw open"><span class="code" style="font-weight:600">E11.36</span><span class="cond">Type 2 Diabetes Mellitus</span><span>18</span><span class="raf">0.302</span><span class="btn close">Close <span class="tri-r"></span></span></div>
  </div>
  <p class="note" style="left:176px;top:308px;font-size:16px">This patient was treated for <b>CATARACTS</b> that may be associated with <b>TYPE 2 DIABETES MELLITUS</b></p>

  <div class="src" style="left:176px;top:346px;width:772px;height:92px">
    <div class="t" style="left:36px;top:26px;font-size:16px">Extracapsular Cataract with IOL</div>
    <div class="s" style="left:36px;top:50px;font-size:16px">C-CDA : Procedures</div>
    <div class="view" style="left:578px;top:36px;font-size:16px">View Source</div>
    <div class="doc" style="left:691px;top:20px;width:52px;height:52px"><svg width="14" height="18"><use href="#doc"/></svg></div>
  </div>
  <div class="src" style="left:176px;top:455px;width:772px;height:92px">
    <div class="t" style="left:36px;top:26px;font-size:16px">Type 2 Diabetes Mellitus</div>
    <div class="s" style="left:36px;top:50px;font-size:16px">C-CDA : Problem List</div>
    <div class="view" style="left:578px;top:36px;font-size:16px">View Source</div>
    <div class="doc" style="left:691px;top:20px;width:52px;height:52px"><svg width="14" height="18"><use href="#doc"/></svg></div>
  </div>
</section>

<!-- ============ Expanded View A Hover ============ -->
<h2 class="board-title" style="top:1608px">Dashboard 1 - Expanded View A Hover</h2>

<section class="frame bordered" style="top:1686px;height:582px;background:var(--expand)">
  <div class="tbl large" style="top:-19px;--cols:149px 573px 144px 113px 1fr;--pl:19px">
    <div class="rw" style="background:var(--row-b)"><span class="code">F33.1</span><span>Major Deppresive Disorder, Recurrent, Moderate</span><span>58</span><span class="raf">0.309</span><span class="btn">Detail <span class="caret"></span></span></div>
    <div class="rw" style="background:var(--row-a)"><span class="code">148.2</span><span>Chronic Atrial Fibrillation</span><span>96</span><span class="raf">0.268</span><span class="btn">Detail <span class="caret"></span></span></div>
    <div class="rw open"><span class="code" style="font-weight:600">E11.36</span><span class="cond">Type 2 Diabetes Mellitus</span><span>18</span><span class="raf">0.302</span><span class="btn close">Close <span class="tri-r"></span></span></div>
  </div>
  <p class="note" style="left:168px;top:166px;font-size:16px">This patient was treated for <b>CATARACTS</b> that may be associated with <b>TYPE 2 DIABETES MELLITUS</b></p>

  <div class="src" style="left:168px;top:204px;width:762px;height:139px;border:1.5px solid var(--teal)">
    <div class="t" style="left:35px;top:26px;font-size:16px">Cataract</div>
    <div class="s" style="left:35px;top:50px;font-size:16px">Opthalmology Chart Note</div>
    <div class="kv" style="left:35px;top:87px;font-size:16px"><span>Note</span></div>
    <div class="kv" style="left:117px;top:87px;font-size:16px">"Patient presents for Cataract evaluation in the right eye"</div>
    <div class="view" style="left:568px;top:36px;font-size:16px">View Source</div>
    <div class="doc" style="left:680px;top:18px;width:52px;height:52px"><svg width="14" height="18"><use href="#doc"/></svg></div>
  </div>
  <div class="src" style="left:168px;top:363px;width:762px;height:194px;border:1.5px solid var(--teal)">
    <div class="t" style="left:35px;top:26px;font-size:16px">HbA1C</div>
    <div class="s" style="left:35px;top:52px;font-size:16px">Lab Results</div>
    <div class="kv" style="left:35px;top:89px;font-size:16px"><span>Problem</span></div>
    <div class="kv" style="left:117px;top:89px;font-size:16px">Hemoglobin A1C</div>
    <div class="kv" style="left:35px;top:120px;font-size:16px"><span>Info</span></div>
    <div class="kv" style="left:117px;top:120px;font-size:16px">6.9%</div>
    <div class="kv" style="left:35px;top:151px;font-size:16px"><span>Date</span></div>
    <div class="kv" style="left:117px;top:151px;font-size:16px">01-15-2021</div>
    <div class="view" style="left:568px;top:34px;font-size:16px">View Source</div>
    <div class="doc" style="left:680px;top:18px;width:52px;height:52px"><svg width="14" height="18"><use href="#doc"/></svg></div>
  </div>
</section>

<!-- ============ Expanded View A Presentation ============ -->
<h2 class="board-title" style="top:2304px">Dashboard 1 - Expanded View A Presentation</h2>

<section class="frame bordered" style="top:2381px;height:581px">
  <nav class="sidebar" style="top:0">
    <div class="nav-item" style="top:-13px"><i><b></b></i>Tutorial</div>
  </nav>
  <div class="tbl small" style="top:-27px">
    <div class="rw" style="background:var(--row-a);height:44px"><span class="code">148.2</span><span>Chronic Atrial Fibrillation</span><span>96</span><span class="raf">0.268</span><span class="btn">Detail <span class="caret"></span></span></div>
    <div class="rw open" style="height:44px"><span class="code" style="font-weight:600">E11.36</span><span class="cond">Type 2 Diabetes Mellitus</span><span>18</span><span class="raf">0.302</span><span class="btn close">Close <span class="tri-r"></span></span></div>
  </div>
  <div class="abs" style="left:247px;top:17px;width:856px;height:564px;background:var(--expand)"></div>
  <p class="note" style="left:378px;top:80px;font-size:11.5px">This patient was treated for <b>CATARACTS</b> that may be associated with <b>TYPE 2 DIABETES MELLITUS</b></p>

  <div class="src" style="left:378px;top:112px;width:536px;height:68px">
    <div class="t" style="left:26px;top:17px;font-size:11.5px">Extracapsular Cataract with IOL</div>
    <div class="s" style="left:26px;top:36px;font-size:11.5px">C-CDA : Procedures</div>
    <div class="view" style="left:436px;top:24px;font-size:11.5px">View Source</div>
    <div class="doc" style="left:522px;top:16px;width:36px;height:36px"><svg width="11" height="14"><use href="#doc"/></svg></div>
  </div>
  <div class="src glow" style="left:389px;top:185px;width:662px;height:121px">
    <div class="t" style="left:30px;top:21px;font-size:14px">Cataract</div>
    <div class="s" style="left:30px;top:41px;font-size:14px">Opthalmology Chart Note</div>
    <div class="kv" style="left:30px;top:75px;font-size:14px"><span>Note</span></div>
    <div class="kv" style="left:103px;top:75px;font-size:14px">"Patient presents for Cataract evaluation in the right eye"</div>
    <div class="view" style="left:497px;top:29px;font-size:14px">View Source</div>
    <div class="doc" style="left:593px;top:16px;width:46px;height:46px"><svg width="13" height="17"><use href="#doc"/></svg></div>
  </div>

  <div class="src" style="left:378px;top:344px;width:536px;height:65px">
    <div class="t" style="left:26px;top:17px;font-size:11.5px">Type 2 Diabetes Mellitus</div>
    <div class="s" style="left:26px;top:35px;font-size:11.5px">C-CDA : Problem List</div>
    <div class="view" style="left:436px;top:23px;font-size:11.5px">View Source</div>
    <div class="doc" style="left:522px;top:15px;width:36px;height:36px"><svg width="11" height="14"><use href="#doc"/></svg></div>
  </div>
  <div class="src glow" style="left:389px;top:417px;width:660px;height:190px">
    <div class="t" style="left:30px;top:17px;font-size:14px">HbA1C</div>
    <div class="s" style="left:30px;top:38px;font-size:14px">Lab Results</div>
    <div class="kv" style="left:30px;top:70px;font-size:14px"><span>Problem</span></div>
    <div class="kv" style="left:103px;top:70px;font-size:14px">Hemoglobin A1C</div>
    <div class="kv" style="left:30px;top:97px;font-size:14px"><span>Info</span></div>
    <div class="kv" style="left:103px;top:97px;font-size:14px">6.9%</div>
    <div class="kv" style="left:30px;top:124px;font-size:14px"><span>Date</span></div>
    <div class="kv" style="left:103px;top:124px;font-size:14px">01-15-2021</div>
    <div class="view" style="left:497px;top:26px;font-size:14px">View Source</div>
    <div class="doc" style="left:593px;top:14px;width:46px;height:46px"><svg width="13" height="17"><use href="#doc"/></svg></div>
  </div>
</section>

<!-- ============ Expanded View B ============ -->
<h2 class="board-title" style="top:2998px">Dashboard 1 - Expanded View B</h2>

<section class="frame" style="top:3077px;height:1082px">
  <div class="topbar">
    <div class="brand-mark"></div>
    <div class="brand-name">CareLedger</div>
    <div class="tagline">Each patients' full medical history, summary and analysis in one comprehensive health record</div>
    <svg class="apps" width="16" height="16"><use href="#grid"/></svg>
    <div class="badge">27</div>
    <div class="avatar"></div>
    <div class="user">Lina Admin <span class="caret"></span></div>
  </div>
  <nav class="sidebar">
    <div class="side-label" style="top:33px">Main</div>
    <div class="nav-item" style="top:56px"><i><b></b></i>Dashboard</div>
    <div class="nav-item" style="top:99px"><i><b></b></i>Employee</div>
    <div class="nav-item" style="top:143px"><i><b></b></i>Document</div>
    <div class="nav-item" style="top:187px"><i><b></b></i>Appointment</div>
    <div class="nav-item" style="top:230px"><i><b></b></i>Surveillance</div>
    <div class="nav-item active" style="top:274px"><i><b></b></i>Reports</div>
    <div class="side-label" style="top:333px">Support</div>
    <div class="nav-item" style="top:367px"><i><b></b></i>Settings</div>
    <div class="nav-item" style="top:411px"><i><b></b></i>Tutorial</div>
  </nav>

  <div class="crumb-icon"><svg width="14" height="14"><use href="#tiles"/></svg></div>
  <div class="crumb"><span class="lnk">Reports</span> <span style="font-size:13px">▶</span> C-CDA Compendium</div>
  <div class="print"><svg width="16" height="16"><use href="#printer"/></svg></div>
  <div class="idsearch">Type ID Number here <span class="sel">ID Number <span class="caret"></span></span><span class="sbtn"><svg width="11" height="11"><use href="#mag"/></svg></span></div>

  <div class="profile"><span class="k">Patient Profile</span>&nbsp;&nbsp; Nora Vale | Female | 70 Years Old | 01-11-1951</div>
  <div class="updated"><span class="k">Last Updated:</span> May 24, 2021</div>

  <div class="stat raf"><div class="lbl">R A F</div><div class="val">1.462</div><div class="ic"></div></div>
  <div class="stat cond"><div class="lbl">Condition</div><div class="val">5</div><div class="ic"></div></div>
  <div class="stat idn"><div class="lbl">ID Number</div><div class="val" style="letter-spacing:1px">7326472</div><div class="ic"></div></div>

  <div class="hcc">▾ HCC Summary</div>
  <div class="section" style="top:329px">Newly Identified ICD-10 Code</div>
  <div class="mini-search" style="top:320px">Search<span class="sbtn"><svg width="10" height="10"><use href="#mag"/></svg></span></div>

  <div class="tbl small" style="top:367px">
    <div class="hd"><span>ICD-10 CODE <span class="caret"></span></span><span>CONDITION <span class="caret"></span></span><span>CATEGORY <span class="caret"></span></span><span>RAF <span class="caret"></span></span><span>ACTION</span></div>
    <div class="rw"><span class="code">170.0</span><span>Aortic Atherosclerosis</span><span>108</span><span class="raf">0.298</span><span class="btn">Detail <span class="caret"></span></span></div>
    <div class="rw"><span class="code">F33.1</span><span>Major Deppresive Disorder, Recurrent, Moderate</span><span>58</span><span class="raf">0.309</span><span class="btn">Detail <span class="caret"></span></span></div>
    <div class="rw"><span class="code">148.2</span><span>Chronic Atrial Fibrillation</span><span>96</span><span class="raf">0.268</span><span class="btn">Detail <span class="caret"></span></span></div>
    <div class="rw open" style="height:412px;align-items:start;padding-top:12px"><span class="code" style="font-weight:600">N18.31</span><span class="cond">Chronic Kidney Disease, Stage 3A</span><span>138</span><span class="raf">0.069</span><span class="btn close">Close <span class="tri-r"></span></span></div>
  </div>
  <p class="note" style="left:378px;top:589px;font-size:11.5px">This patient has an <b>eGFR</b> between <b>45-59 mL/min</b></p>

  <div class="src" style="left:378px;top:619px;width:585px;height:310px;font-size:11.5px">
    <div class="t" style="left:26px;top:19px;font-weight:600">eGFR</div>
    <div class="s" style="left:26px;top:38px;font-weight:500">Lab Results</div>
    <div class="kv" style="left:26px;top:67px"><span>Problem</span></div>
    <div class="kv" style="left:90px;top:67px">eGFR</div>
    <div class="kv" style="left:26px;top:90px"><span>Info</span></div>
    <div class="kv" style="left:90px;top:90px">47 mL/min</div>
    <div class="kv" style="left:26px;top:114px"><span>Date</span></div>
    <div class="kv" style="left:90px;top:114px">05-26-2021</div>
    <div class="s" style="left:26px;top:151px;font-weight:600">History</div>
    <div class="kv" style="left:26px;top:180px"><span>Info</span></div>
    <div class="kv" style="left:126px;top:180px"><span>Date</span></div>
    <div class="kv" style="left:26px;top:201px">45 mL/min</div>
    <div class="kv" style="left:126px;top:201px">03-17-2021</div>
    <div class="kv" style="left:26px;top:220px">41 mL/min</div>
    <div class="kv" style="left:126px;top:220px">01-12-2021</div>
    <div class="kv" style="left:26px;top:240px">52 mL/min</div>
    <div class="kv" style="left:126px;top:240px">10-15-2020</div>
    <div class="kv" style="left:26px;top:259px">44 mL/min</div>
    <div class="kv" style="left:126px;top:259px">06-22-2020</div>
    <div class="view" style="left:436px;top:19px">View Source</div>
    <div class="doc" style="left:522px;top:11px;width:36px;height:36px"><svg width="11" height="14"><use href="#doc"/></svg></div>
  </div>

  <div class="pager" style="left:898px;top:970px">Show Row <span class="sel">5 <span class="caret" style="margin-left:3px"></span></span><span class="pg"><span class="tri-l"></span></span><span class="pg next"><span class="tri-r"></span></span></div>

  <div class="section" style="top:1032px">Previously Known ICD-10 Code</div>
  <div class="mini-search" style="top:1026px">Search<span class="sbtn"><svg width="10" height="10"><use href="#mag"/></svg></span></div>
  <div class="abs" style="left:247px;top:1070px;width:856px;height:20px;background:var(--row-head)"></div>
</section>

</body>
</html>
```